A new website for Electrical Contractor Business

We are looking for a unique and new WordPress website design which would include 5 Pages - Home Page, Meet the Team, Our Services, Our Projects and Contact Us page.

The global theme for the website needs to be professional but simple to navigate as we cater for both business and home owner customers.

Our core business service is targeted around lighting from single room decorative to large office so the theme should incorporate this in some way.

The home page should include;
Our business logo, Contact number, Email address, small Image rotation box - Highlighting pervious projectsText box - With welcome message, chirpnet feed news reel/Customer feed back box.

I would also like to see a 2 boxes for the separate customer types we services. Business and Home Owner. each box will have a small image with a small text description with a link to the area of the services page relevant to that customer type.

Meet the team page -This will be introducing potential customers to the team so I would like it to include for each team member. Something like a small image and text area which will introduce an outline of the team members skills and abilities.

Our Services page This page will be outlining the different services on offer to the both customer types business and homeowner. Each service should have an image with text description of the service would good here.

Our projects page-Will include images of pervious projects and work we have completed along with a text area for the project description/ outliner.

Contact Us page - Should include a contact form which should include an option for the customer to quest us to call them back, also a selection box for them to inform us our how they found our details would be good.

Colour - The theme colours can be taken from the logo or feel free to impress with your own imagination.

Remember we are looking for a website that will interest our customers enough to except our services or be drawn further into the website.. So call to action links to other areas of the site/ contact page are welcome

Target Market(s)

Business - Office, warehousing and Large Store - lighting and Power
Home owner lighting and power

Coding

Coded - Design and coding required

Number of Pages Required

5+ page

Font styles to use
Serif
Sans Serif

Colors

Designer to choose colors to be used in the design.

Requirements
Must have
• Logo integrated into the website design - i.e. website colours which allow the logo to blend into the design.
Nice to have
• Custom but professional theme catering to business customers, but also show that we do provide services to home owners too.
Should not have
• Sorry am not interested in one oversized block image on rotation covering half the home page.. Images will be needed but not a single block over sized frame with not text, shape. Please use your imagination when considering this design

```html
<!DOCTYPE html>
<html lang="en">
<head>
<meta charset="utf-8">
<title>Brightwire Electrical – Home</title>
<link rel="stylesheet" href="https://fonts.googleapis.com/css2?family=Montserrat:wght@400;600;700;800&family=Open+Sans:wght@400;600&display=swap">
<style>
:root{
  --navy:#1d3461;
  --navy-dark:#14264a;
  --orange:#ee6a2a;
  --orange-dark:#d9561a;
  --ink:#3b4252;
  --muted:#7a8190;
  --light:#f3f5f8;
  --white:#ffffff;
}
*{box-sizing:border-box;margin:0;padding:0}
html,body{width:1200px;height:2564px;overflow:hidden}
body{font-family:"Open Sans",sans-serif;color:var(--ink);background:var(--white);position:relative}
h1,h2,h3,h4,.nav,.btn{font-family:"Montserrat",sans-serif}
a{text-decoration:none;color:inherit}

.topbar{height:28px;background:var(--navy-dark);color:#c9d2e3;font-size:11px;display:flex;align-items:center;padding:0 72px;gap:22px}
.topbar span b{color:var(--orange);font-weight:600}

.header{height:84px;display:flex;align-items:center;padding:0 60px;justify-content:space-between;background:var(--white)}
.brand{display:flex;align-items:center;gap:10px;font-family:"Montserrat",sans-serif;font-weight:800;font-size:22px;color:var(--navy);letter-spacing:.5px}
.brand i{width:38px;height:38px;border-radius:50%;background:var(--orange);display:block}
.nav{display:flex;gap:34px;font-size:14px;font-weight:600;color:var(--navy)}
.nav a.active{color:var(--orange)}
.phone-btn{background:var(--orange);color:#fff;font-weight:700;font-size:13px;padding:9px 16px;border-radius:3px;display:flex;gap:8px;align-items:center}

.hero{position:relative;height:290px;overflow:hidden}
.hero-photo{position:absolute;inset:0;background:
  radial-gradient(ellipse 260px 200px at 860px 130px,rgba(238,106,42,.35),transparent 70%),
  radial-gradient(ellipse 360px 260px at 760px 110px,#e4e7ed,transparent 70%),
  linear-gradient(100deg,#263f6b 0%,#4d6690 38%,#aab4c6 62%,#d3d7df 78%,#7f8aa0 100%)}
.hero-copy{position:absolute;left:110px;top:50px;width:440px;color:#fff}
.hero-copy h1{font-size:29px;line-height:1.25;font-weight:700}
.hero-arrow{position:absolute;top:130px;width:22px;height:30px;background:rgba(20,38,74,.7);display:flex;align-items:center;justify-content:center}
.hero-wave{position:absolute;left:0;bottom:0;width:1200px;height:70px}

.btn{display:inline-block;font-size:12px;font-weight:600;color:#fff;padding:8px 18px;border-radius:16px}
.btn-orange{background:var(--orange)}
.btn-navy{background:var(--navy)}

.welcome{position:relative;height:460px;padding:100px 0 0 140px}
.welcome h2{font-size:30px;font-weight:800;color:var(--navy);display:flex;align-items:center;gap:12px}
.welcome h2 .brand{font-size:20px}
.welcome h2 .brand i{width:30px;height:30px}
.welcome p{width:520px;font-size:13.5px;line-height:1.7;color:var(--muted);margin:22px 0 22px}
.welcome-disc{position:absolute;right:130px;top:70px;width:300px;height:300px;border-radius:50%;background:
  radial-gradient(circle at 30% 30%,#f1f3f6,transparent 45%),
  radial-gradient(circle at 60% 75%,rgba(238,106,42,.45),transparent 35%),
  linear-gradient(135deg,#c7ccd6,#1d3461 70%)}

.customers{display:flex;justify-content:center;gap:34px;height:248px;position:relative}
.cust{display:flex;width:432px;height:228px}
.cust-photo{width:216px;height:228px}
.cust-text{width:216px;color:#fff;padding:30px 22px;text-align:center}
.cust-text h3{font-size:17px;margin:10px 0 10px}
.cust-text p{font-size:12px;line-height:1.6}
.icon-box{width:40px;height:40px;margin:0 auto;border:2px solid #fff;border-radius:4px}
.join{position:absolute;left:584px;top:96px;width:32px;height:32px;border-radius:50%;background:#fff;border:3px solid var(--navy)}

.projects{position:absolute;left:0;top:1192px;width:1200px;height:560px;background:var(--navy);text-align:center;padding-top:62px}
.section-title{font-size:28px;font-weight:700;letter-spacing:1px}
.projects .section-title{color:#fff}
.projects .section-title em{font-style:normal;color:var(--orange)}
.filters{display:flex;justify-content:center;gap:8px;margin:34px 0 30px}
.filters a{font-family:"Montserrat",sans-serif;font-size:13px;font-weight:600;color:#fff;padding:8px 16px;border:1px solid #5a6f98}
.filters a.on{background:var(--orange);border-color:var(--orange)}
.gallery{display:flex;justify-content:center;gap:10px}
.tile{width:224px}
.tile-photo{height:92px}
.tile-cap{background:var(--orange);color:#fff;font-weight:600;font-size:13px;padding:7px 0;font-family:"Montserrat",sans-serif}

.review{position:absolute;left:280px;top:1660px;width:640px;height:214px;background:#fff;box-shadow:0 6px 22px rgba(0,0,0,.16);display:flex;gap:26px;padding:28px}
.review-photo{width:140px;height:158px;flex:none;background:radial-gradient(circle at 50% 35%,#d9dee7,transparent 45%),linear-gradient(160deg,#b8c1d1,#5d6f91)}
.review blockquote{font-size:13px;line-height:1.7;color:var(--muted);position:relative;padding-left:48px}
.review blockquote::before{content:"\201C";position:absolute;left:0;top:-24px;font-size:80px;color:#d7dbe3;font-family:Georgia,serif}
.review cite{display:block;font-style:normal;font-weight:600;color:var(--navy);margin-top:10px;font-size:12px}
.slide-arrow{position:absolute;top:1750px;width:36px;height:36px;border-radius:50%;border:1px solid #c5cbd6;background:#fff;display:flex;align-items:center;justify-content:center}
.more{position:absolute;left:0;top:1990px;width:1200px;text-align:center;font-size:14px;font-weight:600;color:var(--navy);font-family:"Montserrat",sans-serif}

.why{position:absolute;left:0;top:2056px;width:1200px;text-align:center}
.why .section-title{color:var(--navy)}
.why .section-title em{font-style:normal;color:var(--orange)}
.why p{font-size:15px;line-height:1.7;color:var(--muted);margin-top:14px}
.why a{display:inline-block;margin-top:10px;color:var(--orange);font-weight:600;font-size:13px;border-bottom:1px solid var(--orange);font-family:"Montserrat",sans-serif}

.footer{position:absolute;top:2236px;left:0;width:1200px;height:292px}
.footer-bg{position:absolute;inset:0;width:1200px;height:292px}
.footer-cols{position:absolute;top:76px;left:140px;display:flex;color:#fff}
.fcol h4{font-size:14px;margin-bottom:14px}
.fcol ul{list-style:none;font-size:12px;line-height:2}
.fcol.links{width:230px}
.fcol.contact{width:260px}
.fcol.contact li{display:flex;gap:8px;align-items:center}
.fcol.feed{width:260px}
.fcol.feed p{font-size:12px;line-height:1.7}
.fcol.feed .feed-head{display:flex;align-items:center;justify-content:space-between}
.fcol.feed .feed-head i{width:22px;height:22px;border-radius:50%;background:var(--navy);display:block;margin-bottom:14px}
.foot-brand{position:absolute;right:120px;top:66px;width:150px;height:150px;border-radius:50%;border:3px solid #fff;display:flex;align-items:center;justify-content:center;color:#fff;font-family:"Montserrat",sans-serif;font-weight:800;font-size:15px;text-align:center;line-height:1.3}
.bottombar{position:absolute;top:2528px;left:0;width:1200px;height:36px;background:var(--navy-dark);color:#aeb9cf;font-size:11px;display:flex;align-items:center;justify-content:space-between;padding:0 72px}
.bottombar .social{display:flex;gap:10px}
.bottombar .social i{width:12px;height:12px;background:#aeb9cf;border-radius:2px;display:block}
</style>
</head>
<body>

<div class="topbar">
  <span><b>CALL</b> 0123 456 7890</span>
  <span><b>EMAIL</b> hello@brightwire.example</span>
</div>

<header class="header">
  <a class="brand" href="#"><i></i>Brightwire Electrical</a>
  <nav class="nav">
    <a class="active" href="#">Home</a>
    <a href="#">Our Services</a>
    <a href="#">Meet Our Team</a>
    <a href="#">Projects</a>
    <a href="#">Contact Us</a>
  </nav>
  <a class="phone-btn" href="#">
    <svg width="12" height="12" viewBox="0 0 24 24" fill="#fff"><path d="M6.6 10.8a15 15 0 0 0 6.6 6.6l2.2-2.2a1 1 0 0 1 1-.25 11 11 0 0 0 3.6.6 1 1 0 0 1 1 1V20a1 1 0 0 1-1 1A17 17 0 0 1 3 4a1 1 0 0 1 1-1h3.5a1 1 0 0 1 1 1c0 1.25.2 2.45.6 3.6a1 1 0 0 1-.25 1z"/></svg>
    0123 456 7890
  </a>
</header>

<section class="hero">
  <div class="hero-photo" role="img" aria-label="Electrician working on wiring with a screwdriver"></div>
  <div class="hero-copy">
    <h1>We Provide A Trustworthy, Reliable, And Professional Team of Qualified Electricians</h1>
    <a class="btn btn-orange" href="#" style="margin-top:18px">Contact Us Today</a>
  </div>
  <div class="hero-arrow" style="left:0"><svg width="8" height="12" viewBox="0 0 8 12"><path d="M7 1 2 6l5 5" stroke="#fff" stroke-width="2" fill="none"/></svg></div>
  <div class="hero-arrow" style="right:0"><svg width="8" height="12" viewBox="0 0 8 12"><path d="M1 1l5 5-5 5" stroke="#fff" stroke-width="2" fill="none"/></svg></div>
  <svg class="hero-wave" viewBox="0 0 1200 70" preserveAspectRatio="none">
    <path d="M0 40 Q600 -10 1200 40 L1200 70 L0 70Z" fill="var(--orange)"/>
    <path d="M0 56 Q600 10 1200 56 L1200 70 L0 70Z" fill="#fff"/>
  </svg>
</section>

<section class="welcome">
  <h2>WELCOME TO <span class="brand"><i></i>Brightwire Electrical</span></h2>
  <p>Lorem ipsum dolor sit amet, consectetuer adipiscing elit, sed diam nonummy nibh euismod tincidunt ut laoreet dolore magna aliquam erat volutpat. Ut wisi enim ad minim veniam, quis nostrud exerci tation ullamcorper suscipit lobortis nisl ut aliquip ex ea commodo consequat. Duis autem vel eum iriure dolor in hendrerit in vulputate velit esse molestie consequat, vel illum dolore eu feugiat nulla facilisis at vero eros et accumsan et iusto odio dignissim qui blandit praesent luptatum zzril delenit augue duis dolore te.</p>
  <a class="btn btn-navy" href="#">Contact Us Today</a>
  <div class="welcome-disc" role="img" aria-label="Round photo of a lit office interior"></div>
</section>

<section class="customers">
  <div class="cust">
    <div class="cust-photo" role="img" aria-label="Lit family home at dusk" style="background:radial-gradient(ellipse at 50% 75%,#f0b060,transparent 55%),linear-gradient(170deg,#1f3358 0%,#34507e 45%,#6d5638 80%,#2a2418 100%)"></div>
    <div class="cust-text" style="background:var(--navy)">
      <div class="icon-box"></div>
      <h3>Residential</h3>
      <p>Lorem ipsum dolor sit amet, consectetuer adipiscing elit, sed diam nonummy nibh euismod tincidunt.</p>
    </div>
  </div>
  <div class="join"></div>
  <div class="cust">
    <div class="cust-text" style="background:var(--orange)">
      <div class="icon-box"></div>
      <h3>Commercial</h3>
      <p>Lorem ipsum dolor sit amet, consectetuer adipiscing elit, sed diam nonummy nibh euismod tincidunt.</p>
    </div>
    <div class="cust-photo" role="img" aria-label="Bright open-plan office with ceiling lights" style="background:radial-gradient(ellipse at 50% 15%,#ffffff,transparent 50%),linear-gradient(180deg,#e6e9ef 0%,#b4bccb 55%,#6f7d96 100%)"></div>
  </div>
</section>

<section class="projects">
  <h2 class="section-title">PROJECTS <em>GALLERY</em></h2>
  <div class="filters">
    <a class="on" href="#">All</a><a href="#">Domestic</a><a href="#">Commercial</a><a href="#">Others</a>
  </div>
  <div class="gallery">
    <div class="tile"><div class="tile-photo" role="img" aria-label="Warehouse with high-bay lighting" style="background:radial-gradient(ellipse at 50% 20%,#eef0f4,transparent 55%),linear-gradient(#c9ced8,#5f6b82)"></div><div class="tile-cap">Lorem Ipsum Dolor</div></div>
    <div class="tile"><div class="tile-photo" role="img" aria-label="Office corridor lighting" style="background:radial-gradient(ellipse at 50% 30%,#ffffff,transparent 55%),linear-gradient(#e7eaf0,#8090ad)"></div><div class="tile-cap">Lorem Ipsum Dolor</div></div>
    <div class="tile"><div class="tile-photo" role="img" aria-label="Warm lit retail interior" style="background:radial-gradient(ellipse at 50% 40%,#fbe6b8,transparent 55%),linear-gradient(#d8b676,#6e5230)"></div><div class="tile-cap">Lorem Ipsum Dolor</div></div>
    <div class="tile"><div class="tile-photo" role="img" aria-label="Decorative ceiling light installation" style="background:radial-gradient(ellipse at 50% 25%,#fff2d4,transparent 55%),linear-gradient(#efd9a8,#9c7a48)"></div><div class="tile-cap">Lorem Ipsum Dolor</div></div>
  </div>
</section>

<article class="review">
  <div class="review-photo" role="img" aria-label="Customer portrait"></div>
  <blockquote>Lorem ipsum dolor sit amet, consectetuer adipiscing elit, sed diam nonummy nibh euismod tincidunt ut laoreet dolore magna aliquam erat volutpat. Ut wisi enim ad minim veniam, quis nostrud exerci tation.
    <cite>Lorem Nequme</cite>
  </blockquote>
</article>
<div class="slide-arrow" style="left:176px"><svg width="8" height="12" viewBox="0 0 8 12"><path d="M7 1 2 6l5 5" stroke="#7a8190" stroke-width="2" fill="none"/></svg></div>
<div class="slide-arrow" style="left:988px"><svg width="8" height="12" viewBox="0 0 8 12"><path d="M1 1l5 5-5 5" stroke="#7a8190" stroke-width="2" fill="none"/></svg></div>
<a class="more" href="#">Read More Reviews + Success Stories &rarr;</a>

<section class="why">
  <h2 class="section-title"><em>WHY</em> CHOOSE US</h2>
  <p>Lighting design and application are paramount in our company's services.<br>Industry leading product use &amp; integration are always on the forefront with our customer client services.</p>
  <a href="#">SCHEDULE YOUR SERVICE TODAY</a>
</section>

<footer class="footer">
  <svg class="footer-bg" viewBox="0 0 1200 292" preserveAspectRatio="none">
    <path d="M0 30 Q600 -20 1200 30 L1200 292 L0 292Z" fill="var(--orange)"/>
  </svg>
  <div class="footer-cols">
    <div class="fcol links">
      <h4>Quick Links</h4>
      <ul><li>Home</li><li>Our Services</li><li>Meet Our Team</li><li>Projects</li><li>Contact Us</li></ul>
    </div>
    <div class="fcol contact">
      <h4>Contact Details</h4>
      <ul>
        <li><svg width="12" height="12" viewBox="0 0 24 24" fill="#fff"><path d="M12 2a7 7 0 0 0-7 7c0 5 7 13 7 13s7-8 7-13a7 7 0 0 0-7-7zm0 9.5A2.5 2.5 0 1 1 12 6.5a2.5 2.5 0 0 1 0 5z"/></svg>12 Lumen Street, Northfield</li>
        <li><svg width="12" height="12" viewBox="0 0 24 24" fill="#fff"><path d="M2 5h20v14H2zm2 2v.5l8 5 8-5V7z"/></svg>hello@brightwire.example</li>
        <li><svg width="12" height="12" viewBox="0 0 24 24" fill="#fff"><path d="M6.6 10.8a15 15 0 0 0 6.6 6.6l2.2-2.2a1 1 0 0 1 1-.25 11 11 0 0 0 3.6.6 1 1 0 0 1 1 1V20a1 1 0 0 1-1 1A17 17 0 0 1 3 4a1 1 0 0 1 1-1h3.5a1 1 0 0 1 1 1c0 1.25.2 2.45.6 3.6a1 1 0 0 1-.25 1z"/></svg>0123 456 7890</li>
      </ul>
    </div>
    <div class="fcol feed">
      <div class="feed-head"><h4>Chirpnet Feeds</h4><i></i></div>
      <p>Lorem ipsum dolor sit amet consectetuer adipiscing elit, sed diam nonummy nibh euismod tincidunt laoreet dolore magna.</p>
      <p style="margin-top:6px;font-weight:600">View All</p>
    </div>
  </div>
  <div class="foot-brand">Brightwire<br>Electrical</div>
</footer>

<div class="bottombar">
  <span>Copyright &copy; 2024 Brightwire Electrical | All Rights Reserved</span>
  <div class="social"><i></i><i></i><i></i></div>
</div>

</body>
</html>
```